Corporate Design für Sachverständigerbüro
Zielgruppe
freiberufliche Tätigkeit als öffentlich bestellter und vereidigter Sachverständiger
Erstellung von landwirtschaftlichen und insolvenzspezifischen Gutachten, betriebswirtschaftliche Beratung, Betriebsfortführung, Unternehmensbewertung
Zielgruppe: Insovenzverwalter, Rechtsanwälte, Steuerberater, Landwirte
Aufgabenstellung
Nennung des Names, der öffentlichen Bestellung sowie Sachverständigenbüro Harald Kessing;
Gerne dunkelgrüne Logoelemente; Logo eher schlicht; Deisign sollte Seriösität, Vertrauen und Fachkompetenz kommunizieren

```html
<!DOCTYPE html>
<html lang="de">
<head>
<meta charset="utf-8">
<title>Corporate Design – Sachverständigenbüro Harald Kessing</title>
<link href="https://fonts.googleapis.com/css2?family=Montserrat:wght@500;600&family=Open+Sans:wght@400;600&display=swap" rel="stylesheet">
<style>
  :root {
    --backdrop: #8c8b90;
    --paper: #f5f5f3;
    --slate: #3a4d5c;
    --cream: #e7e5d9;
    --ink: #3b3f44;
    --ink-soft: #6d7278;
    --on-dark: #f2f4f5;
  }
  * { margin: 0; padding: 0; box-sizing: border-box; }
  html, body { width: 1200px; height: 800px; overflow: hidden; }
  body {
    background: var(--backdrop);
    font-family: "Open Sans", sans-serif;
    color: var(--ink);
    position: relative;
  }

  /* Wordmark */
  .wordmark { display: flex; align-items: center; gap: 10px; }
  .wordmark__square { width: 12px; height: 12px; background: var(--slate); flex: none; }
  .wordmark__text { font-family: "Montserrat", sans-serif; font-weight: 600; color: var(--slate); line-height: 1.05; letter-spacing: .02em; text-transform: uppercase; }
  .wordmark__sub { font-family: "Montserrat", sans-serif; font-weight: 500; letter-spacing: .22em; text-transform: uppercase; color: var(--slate); }

  /* Letterhead */
  .letterhead {
    position: absolute; left: 60px; top: 30px;
    width: 522px; height: 740px;
    background: var(--paper);
    box-shadow: 0 6px 18px rgba(0,0,0,.22);
  }
  .letterhead__band-left { position: absolute; left: 0; top: 0; width: 7px; height: 300px; background: var(--slate); }
  .letterhead__band-right { position: absolute; right: 0; bottom: 0; width: 7px; height: 260px; background: var(--slate); }
  .letterhead__head { position: absolute; right: 44px; top: 40px; }
  .letterhead__head .wordmark__text { font-size: 15px; }
  .letterhead__head .wordmark__sub { font-size: 5.5px; margin-top: 3px; }
  .letterhead__contact { position: absolute; right: 44px; top: 104px; width: 150px; font-size: 6.5px; line-height: 1.55; color: var(--ink-soft); font-style: normal; }
  .letterhead__sender { position: absolute; left: 48px; top: 150px; font-size: 5.5px; color: var(--ink-soft); }
  .letterhead__body { position: absolute; left: 48px; right: 48px; top: 280px; font-size: 7.2px; line-height: 1.6; color: var(--ink); }
  .letterhead__body p { margin-bottom: 10px; }
  .letterhead__footer { position: absolute; left: 48px; right: 48px; bottom: 36px; display: flex; justify-content: space-between; font-size: 5.8px; line-height: 1.6; color: var(--ink-soft); }

  /* Business cards */
  .card { position: absolute; width: 430px; height: 278px; box-shadow: 0 6px 18px rgba(0,0,0,.25); }
  .card--front { left: 660px; top: 70px; background: var(--slate); display: flex; align-items: center; justify-content: center; }
  .card--front .wordmark__square { background: var(--on-dark); width: 16px; height: 16px; }
  .card--front .wordmark__text { color: var(--on-dark); font-size: 24px; }
  .card--front .wordmark__sub { color: var(--on-dark); font-size: 8px; margin-top: 6px; opacity: .8; }
  .card--back { left: 660px; top: 430px; background: var(--cream); }
  .card--back .card__brand { position: absolute; left: 36px; top: 36px; }
  .card--back .wordmark__text { font-size: 17px; }
  .card--back .wordmark__sub { font-size: 6.5px; margin-top: 4px; }
  .card__person { position: absolute; left: 36px; bottom: 40px; font-size: 9px; line-height: 1.5; }
  .card__person strong { font-weight: 600; color: var(--slate); display: block; }
  .card__contact { position: absolute; left: 200px; bottom: 40px; font-size: 8px; line-height: 1.6; color: var(--ink-soft); font-style: normal; }
</style>
</head>
<body>

<section class="letterhead" aria-label="Briefbogen">
  <div class="letterhead__band-left"></div>
  <div class="letterhead__band-right"></div>

  <header class="letterhead__head">
    <div class="wordmark">
      <span class="wordmark__square"></span>
      <div>
        <div class="wordmark__text">Dipl.-Ing. Agrar<br>Harald Kessing</div>
        <div class="wordmark__sub">Sachverständigenbüro</div>
      </div>
    </div>
  </header>

  <address class="letterhead__contact">
    Lindenweg 12<br>
    48231 Warendorf<br>
    Mobil: 0171 – 482 19 30<br>
    Telefon: 02581 – 94 27 10<br>
    Telefax: 02581 – 94 27 11<br>
    E-Mail: hk@hkessing.de<br>
    Internet: www.hkessing.de
  </address>

  <div class="letterhead__sender">Dipl.-Ing. Harald Kessing · Lindenweg 12 · 48231 Warendorf</div>

  <div class="letterhead__body">
    <p>Lorem Ipsum is simply dummy text of the printing and typesetting industry.</p>
    <p>Lorem Ipsum has been the industry's standard dummy text ever since the 1500s, when an unknown printer took a galley of type and scrambled it to make a type specimen book. It has survived not only five centuries, but also the leap into electronic typesetting, remaining essentially unchanged. It was popularised in the 1960s with the release of transfer sheets containing Lorem Ipsum passages, and more recently with desktop layout software including versions of Lorem Ipsum.</p>
    <p>Lorem Ipsum is simply dummy text of the printing and typesetting industry. Lorem Ipsum has been the industry's standard dummy text ever since the 1500s, when an unknown printer took a galley of type and scrambled it to make a type specimen book. It has survived not only five centuries, but also the leap into electronic typesetting, remaining essentially unchanged. It was popularised in the 1960s with the release of transfer sheets containing Lorem Ipsum passages, and more recently with desktop layout software including versions of Lorem Ipsum. Lorem Ipsum has been the industry's standard dummy text ever since the 1500s, when an unknown printer took a galley of type and scrambled it to make a type specimen book.</p>
    <p>Lorem Ipsum is simply dummy text of the printing and typesetting industry. It has survived not only five centuries, but also the leap into electronic typesetting, remaining essentially unchanged. It was popularised in the 1960s with the release of transfer sheets containing Lorem Ipsum passages, and more recently with desktop layout software including versions of Lorem Ipsum.</p>
  </div>

  <footer class="letterhead__footer">
    <div>E-Mail: hk@hkessing.de<br>Internet: www.hkessing.de</div>
    <div>Registergericht: Warendorf<br>Registernummer: HRB 41 208</div>
    <div>USt-IdNr.: DE 318 462 905<br>Steuernr.: 336/5084/217</div>
    <div>Landbank Warendorf<br>Kto.-Nr.: 47 302 118<br>Bankleitzahl: 400 612 38</div>
  </footer>
</section>

<section class="card card--front" aria-label="Visitenkarte Vorderseite">
  <div class="wordmark">
    <span class="wordmark__square"></span>
    <div>
      <div class="wordmark__text">Dipl.-Ing. Agrar<br>Harald Kessing</div>
      <div class="wordmark__sub">Sachverständigenbüro</div>
    </div>
  </div>
</section>

<section class="card card--back" aria-label="Visitenkarte Rückseite">
  <div class="card__brand wordmark">
    <span class="wordmark__square"></span>
    <div>
      <div class="wordmark__text">Dipl.-Ing. Agrar<br>Harald Kessing</div>
      <div class="wordmark__sub">Sachverständigenbüro</div>
    </div>
  </div>
  <div class="card__person">
    <strong>Dipl.-Ing. Harald Kessing</strong>
    Geschäftsführer
  </div>
  <address class="card__contact">
    Lindenweg 12 · 48231 Warendorf<br>
    Mobil: 0171 – 482 19 30<br>
    Telefon: 02581 – 94 27 10<br>
    E-Mail: hk@hkessing.de<br>
    Internet: www.hkessing.de
  </address>
</section>

</body>
</html>
```